Harborline Wealth Marketing Powerpoint

I would like help in creating a cool looking powerpoint to share with prospects in marketing my financial advisory business.

Target Market(s)

High Net Worth Individuals and Families

Industry/Entity Type

Financial Service

Requirements
Must have
• My logo in the presentation.

```html
<!DOCTYPE html>
<html lang="en">
<head>
<meta charset="utf-8">
<title>Harborline Wealth – Presentation Template</title>
<link href="https://fonts.googleapis.com/css2?family=Arimo:ital,wght@0,400;0,700;1,400&display=swap" rel="stylesheet">
<style>
:root{
  --blue:#3f8ee6;
  --blue-dark:#2f74c8;
  --navy:#1d3552;
  --ink:#222;
  --grey:#666;
  --light:#e9ebee;
  --teal:#2aa3bd;
  --teal-light:#8fd0dc;
  --green:#6e9b2e;
  --green-light:#a9c46a;
  --list:#3a5f8f;
}
*{box-sizing:border-box}
html,body{margin:0;width:1200px;height:2201px;overflow:hidden;background:#fff;font-family:'Arimo',Arial,sans-serif;color:var(--ink)}
.canvas{position:relative;width:1200px;height:2201px}
.slide{position:absolute;width:413px;height:231px;background:#fff;overflow:hidden;box-shadow:2px 3px 5px rgba(0,0,0,.35)}
.col-l{left:92px}.col-r{left:676px}
.abs{position:absolute}
.photo-city{background:linear-gradient(180deg,#c9ced3 0%,#9aa3ab 45%,#5f6a73 62%,#b7bec4 80%,#8e979f 100%)}
.photo-fade{background:linear-gradient(180deg,#e4e6e8 0%,#cfd3d6 50%,#b9bfc4 65%,#dde0e2 100%)}
.topline{position:absolute;left:0;right:0;top:0;height:3px;background:var(--blue)}
.foot{position:absolute;left:0;bottom:0;width:413px;height:14px}
.mark{position:absolute;right:10px;top:6px;color:var(--blue);font-size:8px;font-weight:700;line-height:1.05;text-align:right}
.title{position:absolute;left:29px;top:11px;font-size:13px;color:var(--ink)}
.sub{color:var(--blue-dark);font-weight:700;font-size:8.5px}
.body{font-size:5.6px;line-height:1.4;color:#333}
.logo-big{color:var(--blue);font-weight:700;line-height:1;text-align:center}
.url{font-size:8px;color:#333;text-align:center}

/* feature lists */
.features{position:absolute;margin:0;padding:0;list-style:none;font-weight:700;color:var(--list);font-size:21px}
.features li{position:relative;padding-left:26px;height:29px;line-height:29px;white-space:nowrap}
.features li::before{content:"";position:absolute;left:2px;top:6px;width:15px;height:15px;border:2px solid var(--list);box-shadow:2px 2px 0 var(--list)}
.features li.sub-item{padding-left:80px;height:26px;line-height:26px}
.features li.sub-item::before{left:60px;top:8px;width:8px;height:8px;border:none;background:var(--list);box-shadow:none}

/* service wheel */
.bubble{position:absolute;width:46px;height:46px;margin:-23px 0 0 -23px;border-radius:50%;background:var(--blue);color:#fff;font-size:5.5px;line-height:1.15;display:flex;align-items:center;justify-content:center;text-align:center;padding:3px;box-shadow:0 1px 2px rgba(0,0,0,.25)}

.bar{position:absolute;left:160px;width:205px;height:13px;color:#fff;font-size:5.8px;line-height:13px;padding-left:4px}
.bar.eq{background:var(--teal)}
.bar.fi{background:var(--green)}

.news{position:absolute;height:10px;font-size:5.5px;line-height:10px;text-align:center;background:#eef0f2}
.blist{position:absolute;margin:0;padding:0;list-style:none;font-size:6px;color:var(--blue-dark)}
.blist li{position:relative;padding-left:12px;margin-bottom:6px;line-height:1.2}
.blist li::before{content:"•";position:absolute;left:2px}

.feat-col{position:absolute;width:86px}
.feat-col h4{margin:0 0 3px;font-size:6.5px;color:var(--blue-dark)}
.feat-col p{margin:0;font-size:4.8px;line-height:1.4;color:#444}

.partner{position:absolute;left:158px;width:240px}
.partner .name{font-size:15px;font-weight:700;color:var(--navy);line-height:1}
.partner p{margin:3px 0 0;font-size:5px;line-height:1.35;font-style:italic;color:#333}

.step-label{position:absolute;font-size:7px;font-weight:700;color:#111}
.contact{position:absolute;left:311px;display:flex;gap:8px;font-size:8px;color:#222;line-height:1.2}
.contact svg{flex:none}
.contact-heading{position:absolute;left:180px;top:140px;width:96px;text-align:center;color:#fff;font-weight:700;font-size:19px;line-height:1.25;white-space:nowrap;z-index:2}
</style>
</head>
<body>
<div class="canvas">

<!-- ROW 1 : cover A -->
<section class="slide col-l" style="top:30px">
  <div class="abs photo-city" style="inset:0" role="img" aria-label="Photograph of a suspension bridge and city skyline reflected in water"></div>
  <svg class="abs" style="inset:0" width="413" height="231" viewBox="0 0 413 231"><path d="M202,0 L145,100 Q136,115 145,130 L200,231 H413 V0 Z" fill="#fff"/></svg>
  <div class="abs logo-big" style="left:215px;top:95px;width:170px;font-size:22px">Harborline<br>Wealth</div>
  <div class="abs url" style="left:215px;top:170px;width:170px">www.<b>harborlinewealth</b>.com</div>
</section>

<!-- ROW 1 : cover B -->
<section class="slide col-r" style="top:30px">
  <div class="abs photo-city" style="inset:0" role="img" aria-label="Photograph of a bridge and city skyline fading to grey on the right"></div>
  <svg class="abs" style="inset:0" width="413" height="231" viewBox="0 0 413 231"><path d="M202,0 L145,100 Q136,115 145,130 L200,231 H413 V0 Z" fill="#fff" opacity=".82"/></svg>
  <div class="abs logo-big" style="left:215px;top:95px;width:170px;font-size:22px">Harborline<br>Wealth</div>
  <div class="abs url" style="left:215px;top:170px;width:170px">www.<b>harborlinewealth</b>.com</div>
</section>

<!-- feature text -->
<ul class="features" style="left:117px;top:275px">
  <li>Ratio 16:9</li>
  <li>Full HD</li>
  <li>Custom color pallet</li>
  <li>Custom Font -&nbsp; Easy Change</li>
  <li>Easy to edit, just drag and drop images</li>
</ul>
<ul class="features" style="left:636px;top:275px">
  <li>Can be included up to 50&nbsp; slides;</li>
  <li class="sub-item">Text + images (1,2,3,4) , Text Slides</li>
  <li class="sub-item">Portfolio Slides , blog slides</li>
  <li class="sub-item">Text Slides, infographics</li>
  <li class="sub-item">Data Slides</li>
  <li>In the sample you find 16 slides</li>
</ul>

<!-- ROW 2 : cover C -->
<section class="slide col-l" style="top:447px">
  <div class="abs photo-fade" style="inset:0" role="img" aria-label="Soft grey photograph of a bridge and skyline"></div>
  <div class="abs logo-big" style="left:190px;top:100px;width:210px;font-size:30px">Harborline<br>Wealth</div>
  <div class="abs url" style="left:300px;top:203px;width:100px">www.<b>harborlinewealth</b>.com</div>
</section>

<!-- ROW 2 : relationship -->
<section class="slide col-r" style="top:447px">
  <div class="abs" style="left:0;top:0;width:104px;height:231px;background:var(--blue)"></div>
  <div class="abs" style="left:8px;top:86px;width:90px;color:#fff;font-size:11.5px;text-align:center;line-height:1.35">Harborline Wealth Relationship</div>
  <div class="mark">Harborline<br>Wealth</div>
  <div class="abs" style="left:116px;top:38px;width:270px;font-size:11.5px;line-height:1.3">Harborline Wealth acts with a fiduciary interest to its clients.</div>
  <ul class="abs body" style="left:116px;top:78px;width:280px;margin:0;padding-left:10px;font-size:5px">
    <li>Providing the highest level of wealth advisory services is at the heart of everything we do.</li>
    <li>We love being a trusted advisor to our clients and work hard to cut through all of the noise to deliver exceptional service.</li>
    <li>There are so many financial decisions that impact multiple areas of an individual's balance sheet that focusing on just one or two likely results in a missed opportunity.</li>
    <li>Our goal is to give you the peace of mind that all aspects of your financial picture are being taken care of.</li>
    <li>As an independent Registered Investment Advisor, we follow the highest financial standard with your best interests as our utmost priority.</li>
    <li>We work on a fee-only basis and do not sell commission-based or proprietary products.</li>
    <li>This gives us the freedom to develop your financial plan and investment strategy without biased outside influences.</li>
  </ul>
</section>

<!-- ROW 3 : what we do -->
<section class="slide col-l" style="top:698px">
  <div class="abs photo-fade" style="inset:0" role="img" aria-label="Misty grey landscape photograph"></div>
  <div class="abs" style="left:19px;top:0;width:130px;height:231px;background:rgba(255,255,255,.92)"></div>
  <div class="abs" style="left:30px;top:34px;width:110px;font-size:19px;line-height:1.2;text-align:center">What do<br>we do?</div>
  <div class="abs logo-big" style="left:30px;top:92px;width:110px;font-size:15px">Harborline<br>Wealth</div>
  <div class="abs" style="left:25px;top:158px;width:120px;font-size:8.5px;font-style:italic;text-align:center;line-height:1.3">We have the expertise and experience to provide an exceptional personal wealth relationship</div>
  <svg class="abs" style="inset:0" width="413" height="231" viewBox="0 0 413 231">
    <defs><marker id="ah" viewBox="0 0 10 10" refX="5" refY="5" markerWidth="4" markerHeight="4" orient="auto"><path d="M0,0 L10,5 L0,10 Z" fill="var(--blue)"/></marker></defs>
    <g stroke="var(--blue)" stroke-width="3" marker-end="url(#ah)">
      <line x1="294" y1="100" x2="294" y2="76"/>
      <line x1="306" y1="104" x2="325" y2="86"/>
      <line x1="312" y1="113" x2="336" y2="108"/>
      <line x1="310" y1="124" x2="330" y2="141"/>
      <line x1="300" y1="130" x2="309" y2="154"/>
      <line x1="288" y1="130" x2="279" y2="154"/>
      <line x1="278" y1="124" x2="258" y2="141"/>
      <line x1="276" y1="113" x2="252" y2="108"/>
      <line x1="282" y1="104" x2="263" y2="86"/>
    </g>
  </svg>
  <div class="bubble" style="left:294px;top:32px">Investment Management</div>
  <div class="bubble" style="left:351px;top:52px">Executive Compensation &amp; Benefits</div>
  <div class="bubble" style="left:381px;top:102px">Retirement Planning</div>
  <div class="bubble" style="left:369px;top:163px">Education</div>
  <div class="bubble" style="left:323px;top:200px">Insurance</div>
  <div class="bubble" style="left:263px;top:200px">Philanthropy</div>
  <div class="bubble" style="left:218px;top:163px">Cash Management &amp; Budgeting</div>
  <div class="bubble" style="left:207px;top:102px">Tax Planning &amp; Compliance</div>
  <div class="bubble" style="left:237px;top:52px">Estate Planning / Wealth Transfer</div>
</section>

<!-- ROW 3 : efficient markets chart -->
<section class="slide col-r" style="top:698px">
  <div class="topline"></div>
  <div class="title">The Power of Efficient Markets</div>
  <div class="mark">Harborline<br>Wealth</div>
  <div class="abs sub" style="left:32px;top:43px">Let Markets Work for You</div>
  <div class="abs body" style="left:32px;top:57px;width:115px">The financial markets have rewarded long-term investors. People expect a positive return on the capital they supply, and historically, the equity and bond markets have provided growth of wealth that has more than offset inflation.</div>
  <div class="abs sub" style="left:32px;top:124px;width:110px;line-height:1.4">Consider the Drivers of Returns</div>
  <div class="abs body" style="left:32px;top:152px;width:115px">There is a wealth of academic research into what drives returns. Expected returns depend on current market prices and expected future cash flows. Investors can use this information to pursue higher expected returns in their portfolios.</div>
  <div class="abs" style="left:175px;top:50px;font-size:5.5px;color:#555;line-height:1.3">Growth of a Dollar, 1926–2018<br>(compounded monthly)</div>
  <svg class="abs" style="left:180px;top:55px" width="200" height="160" viewBox="0 0 200 160">
    <polygon points="0,130 20,125 40,118 60,105 80,95 100,78 120,62 140,45 160,28 178,10 178,140 0,140" fill="var(--teal)"/>
    <polygon points="0,130 30,126 60,118 90,108 120,98 150,85 178,72 178,140 0,140" fill="var(--green-light)"/>
    <polygon points="0,132 40,130 80,126 120,120 150,114 178,108 178,140 0,140" fill="var(--green)"/>
    <polygon points="0,134 60,133 120,130 178,126 178,140 0,140" fill="#8b8f93"/>
    <polygon points="10,130 14,146 18,130" fill="var(--teal)"/>
    <g font-size="4" fill="#555"><text x="181" y="12">$20,445</text><text x="181" y="45">$7,025</text><text x="181" y="72">$142</text><text x="181" y="86">$21</text><text x="181" y="105">$14</text>
    <text x="0" y="156">1926</text><text x="35" y="156">1946</text><text x="70" y="156">1966</text><text x="105" y="156">1986</text><text x="140" y="156">2006</text><text x="170" y="156">2018</text></g>
  </svg>
  <svg class="foot" viewBox="0 0 413 14"><g stroke="var(--navy)" stroke-width="1.5"><line x1="2" y1="2" x2="14" y2="14"/><line x1="8" y1="2" x2="20" y2="14"/><line x1="396" y1="2" x2="408" y2="14"/></g><rect x="22" y="10" width="391" height="3" fill="var(--blue)"/></svg>
</section>

<!-- ROW 4 : philosophy -->
<section class="slide col-l" style="top:949px">
  <div class="topline"></div>
  <div class="title">Guiding Investment Philosophy</div>
  <div class="mark">Harborline<br>Wealth</div>
  <svg class="abs" style="left:24px;top:48px" width="32" height="160" viewBox="0 0 32 160">
    <circle cx="15" cy="15" r="14" fill="var(--blue)"/><path d="M10,9 h10 v5 a5,5 0 0 1 -10,0 Z M13,20 h4 v3 h-4Z" fill="#fff"/>
    <circle cx="15" cy="72" r="14" fill="var(--blue)"/><circle cx="14" cy="71" r="5" fill="none" stroke="#fff" stroke-width="2"/><line x1="18" y1="75" x2="22" y2="79" stroke="#fff" stroke-width="2"/>
    <circle cx="15" cy="135" r="14" fill="#bbb"/><circle cx="15" cy="135" r="7" fill="none" stroke="#fff" stroke-width="1.5"/><line x1="8" y1="135" x2="22" y2="135" stroke="#fff"/>
  </svg>
  <div class="abs" style="left:65px;top:42px;width:150px">
    <div style="font-size:6px;font-weight:700">Embrace Market Pricing</div>
    <div class="body" style="color:#999;font-size:5px">The market is an effective information-processing machine. Each day, the world equity markets process billions of dollars in trades between buyers and sellers — and the real-time information they bring helps set prices.</div>
    <div style="font-size:6px;font-weight:700;margin-top:3px">Don't Try to Outguess the Market</div>
    <div class="body" style="color:#999;font-size:5px">The market's pricing power works against mutual fund managers who try to outperform through stock picking or market timing. Only 23% of US equity mutual funds and 8% of fixed income funds have survived and outperformed their benchmarks over the past 20 years.</div>
    <div style="font-size:6px;font-weight:700;margin-top:3px">Resist Chasing Past Performance</div>
    <div class="body" style="color:#999;font-size:5px">Some investors select mutual funds based on their past returns. Yet past performance offers little insight into a fund's future returns. Most funds in the top quartile of previous five-year returns did not maintain a top-quartile ranking in the following five years.</div>
  </div>
  <svg class="abs" style="left:232px;top:40px" width="175" height="180" viewBox="0 0 175 180">
    <rect x="0" y="0" width="40" height="52" fill="var(--navy)"/>
    <polygon points="40,4 67,12 67,40 40,48" fill="var(--teal)" opacity=".6"/>
    <rect x="67" y="2" width="48" height="48" fill="var(--teal)"/>
    <polygon points="115,10 132,14 132,38 115,42" fill="var(--green-light)"/>
    <rect x="132" y="0" width="42" height="52" fill="var(--green-light)"/>
    <g fill="#fff" font-size="5" text-anchor="middle"><text x="20" y="23">All</text><text x="20" y="29">Available</text><text x="20" y="35">Information</text><text x="91" y="23" font-weight="700">$462.8B</text><text x="91" y="29" font-size="3.6">World Equity Trading</text><text x="91" y="34" font-size="3.6">(Daily Average)</text><text x="153" y="29" font-weight="700">Prices</text></g>
    <text x="16" y="66" font-size="4.5" fill="#333">Percentage of Top-Ranked Funds That Stayed on Top</text>
    <line x1="0" y1="69" x2="150" y2="69" stroke="#999" stroke-width=".5"/>
    <rect x="12" y="74" width="30" height="80" fill="#e1e5f0"/><rect x="12" y="74" width="30" height="18" fill="#3b5b9a"/>
    <text x="15" y="82" font-size="6" fill="#fff" font-weight="700">TOP 25</text><text x="23" y="89" font-size="6" fill="#fff" font-weight="700">%</text>
    <line x1="42" y1="74" x2="62" y2="110" stroke="#555" stroke-width=".5"/><line x1="42" y1="92" x2="62" y2="128" stroke="#555" stroke-width=".5"/>
    <rect x="62" y="82" width="100" height="10" fill="#eee"/><rect x="62" y="100" width="22" height="10" fill="var(--teal)"/>
    <text x="140" y="90" font-size="5" fill="var(--teal)">Equity</text><text x="64" y="108" font-size="7" fill="#fff" font-weight="700">21%</text>
    <rect x="62" y="112" width="100" height="10" fill="#eee"/><rect x="62" y="122" width="28" height="10" fill="var(--green)"/>
    <text x="128" y="120" font-size="5" fill="var(--green)">Fixed Income</text><text x="64" y="130" font-size="7" fill="#fff" font-weight="700">28%</text>
    <text x="146" y="140" font-size="5" fill="#333">100%</text>
    <text x="16" y="164" font-size="4" fill="#555">Previous</text><text x="18" y="169" font-size="4" fill="#555">5 Years</text>
    <text x="62" y="160" font-size="4" fill="#555">Funds Remaining in Top Quartile of Returns</text><text x="62" y="165" font-size="4" fill="#555">in the Following 5-Year Period (2008–2018)</text>
  </svg>
  <svg class="foot" viewBox="0 0 413 14"><g stroke="var(--navy)" stroke-width="1.5"><line x1="2" y1="2" x2="14" y2="14"/><line x1="8" y1="2" x2="20" y2="14"/><line x1="396" y1="2" x2="408" y2="14"/></g><rect x="22" y="10" width="391" height="3" fill="var(--blue)"/></svg>
</section>

<!-- ROW 4 : diversification heatmap -->
<section class="slide col-r" style="top:949px">
  <div class="topline"></div>
  <div class="title">The Power of Efficient Markets</div>
  <div class="mark">Harborline<br>Wealth</div>
  <div class="abs" style="left:30px;top:40px;font-size:9.5px">Annual Returns by Market Index</div>
  <div class="abs sub" style="left:31px;top:70px;width:100px;line-height:1.4">Practice Smart Diversification</div>
  <div class="abs" style="left:31px;top:100px;width:95px;font-size:7px;line-height:1.45;color:#333">Holding securities across many market segments can help manage overall risk. But diversifying within your home market may not be enough. Global diversification can broaden your investment universe.</div>
  <div class="abs" style="left:150px;top:63px;width:50px;font-size:3.8px;line-height:1.2;color:var(--navy)">
    <div style="height:13px">US Large Cap</div><div style="height:13px">US Large Cap Value</div><div style="height:13px">US Small Cap</div><div style="height:13px">US Small Cap Value</div><div style="height:13px">US Real Estate</div><div style="height:13px">Intl. Large Cap Value</div><div style="height:13px">Intl. Small Cap Value</div><div style="height:13px">Emerging Markets</div><div style="height:13px">Five-Year US Govt. Fixed</div>
  </div>
  <div class="abs" style="left:196px;top:62px;font-size:3.8px;text-align:center;line-height:1.1">HIGHER<br>RETURN</div>
  <div class="abs" style="left:196px;top:172px;font-size:3.8px;text-align:center;line-height:1.1">LOWER<br>RETURN</div>
  <svg class="abs" style="left:205px;top:74px" width="4" height="96"><line x1="2" y1="0" x2="2" y2="96" stroke="#333" stroke-width=".6"/></svg>
  <div class="abs" style="left:222px;top:55px;width:178px;display:flex;justify-content:space-between;font-size:3.8px"><span>2004</span><span>2006</span><span>2008</span><span>2010</span><span>2012</span><span>2014</span><span>2016</span><span>2018</span></div>
  <svg class="abs" style="left:222px;top:63px" width="178" height="127" viewBox="0 0 178 127">
    <defs><pattern id="heat" width="60" height="42" patternUnits="userSpaceOnUse">
      <rect x="0" y="0" width="12" height="14" fill="var(--teal)"/><rect x="12" y="0" width="12" height="14" fill="#9aa1a7"/><rect x="24" y="0" width="12" height="14" fill="var(--green-light)"/><rect x="36" y="0" width="12" height="14" fill="#5e6770"/><rect x="48" y="0" width="12" height="14" fill="var(--teal-light)"/>
      <rect x="0" y="14" width="12" height="14" fill="#c9ced2"/><rect x="12" y="14" width="12" height="14" fill="var(--green)"/><rect x="24" y="14" width="12" height="14" fill="var(--teal-light)"/><rect x="36" y="14" width="12" height="14" fill="var(--teal)"/><rect x="48" y="14" width="12" height="14" fill="#7d858c"/>
      <rect x="0" y="28" width="12" height="14" fill="var(--green-light)"/><rect x="12" y="28" width="12" height="14" fill="var(--teal)"/><rect x="24" y="28" width="12" height="14" fill="#4f575e"/><rect x="36" y="28" width="12" height="14" fill="#b2d9e0"/><rect x="48" y="28" width="12" height="14" fill="var(--green)"/>
    </pattern></defs>
    <rect width="178" height="127" fill="url(#heat)"/>
  </svg>
  <svg class="foot" viewBox="0 0 413 14"><g stroke="var(--navy)" stroke-width="1.5"><line x1="2" y1="2" x2="14" y2="14"/><line x1="8" y1="2" x2="20" y2="14"/><line x1="396" y1="2" x2="408" y2="14"/></g><rect x="22" y="10" width="391" height="3" fill="var(--blue)"/></svg>
</section>

<!-- ROW 5 : dimensions of returns -->
<section class="slide col-l" style="top:1200px">
  <div class="topline"></div>
  <div class="title">The Power of Efficient Markets</div>
  <div class="mark">Harborline<br>Wealth</div>
  <div class="abs sub" style="left:26px;top:75px">Avoid Market Timing</div>
  <div class="abs" style="left:26px;top:94px;width:100px;font-size:7px;line-height:1.45;color:#333">You never know which market segments will outperform from year to year. By holding a globally diversified portfolio, investors are well positioned to seek returns wherever they occur.</div>
  <div class="abs" style="left:182px;top:44px;font-size:8.5px;font-weight:700;color:var(--list);text-decoration:underline">Dimensions of Expected Returns</div>
  <div class="abs" style="left:160px;top:61px;font-size:5.8px;color:var(--teal)">EQUITIES</div>
  <div class="bar eq" style="top:75px">Company Size (Market Capitalization)</div>
  <div class="bar eq" style="top:92px">Relative Price (Price/Book Equity)</div>
  <div class="bar eq" style="top:109px">Profitability (Operating Profits/Book Equity)</div>
  <div class="abs" style="left:160px;top:144px;font-size:5.8px;color:var(--green)">FIXED INCOME</div>
  <div class="bar fi" style="top:158px">Term (Sensitivity to Interest Rates)</div>
  <div class="bar fi" style="top:175px">Credit (Credit Quality of Issuer)</div>
  <div class="bar fi" style="top:192px">Currency (Currency of Issuance)</div>
  <svg class="foot" viewBox="0 0 413 14"><g stroke="var(--navy)" stroke-width="1.5"><line x1="2" y1="2" x2="14" y2="14"/><line x1="8" y1="2" x2="20" y2="14"/><line x1="396" y1="2" x2="408" y2="14"/></g><rect x="22" y="10" width="391" height="3" fill="var(--blue)"/></svg>
</section>

<!-- ROW 5 : emotions -->
<section class="slide col-r" style="top:1200px">
  <div class="topline"></div>
  <div class="title">Behavioral Finance…Beware of Your Emotions</div>
  <div class="mark">Harborline<br>Wealth</div>
  <div class="abs sub" style="left:27px;top:51px">Manage Your Emotions</div>
  <div class="abs" style="left:27px;top:66px;width:370px;font-size:6.5px;line-height:1.4;color:#333">Many people struggle to separate their emotions from investing. Markets go up and down. Reacting to current market conditions may lead to making poor investment decisions.</div>
  <svg class="abs" style="inset:0" width="413" height="231" viewBox="0 0 413 231">
    <line x1="48" y1="154" x2="372" y2="154" stroke="#888" stroke-width="1.5" stroke-dasharray="9 5"/>
    <polyline points="67,152 134,122 201,152 272,179 339,150" fill="none" stroke="var(--blue-dark)" stroke-width="1.5"/>
    <g fill="var(--blue-dark)"><circle cx="67" cy="152" r="4"/><circle cx="134" cy="122" r="4"/><circle cx="201" cy="152" r="4"/><circle cx="272" cy="179" r="4"/><circle cx="339" cy="150" r="4"/></g>
    <g font-size="9" fill="#333"><text x="27" y="143">Optimism</text><text x="143" y="113">Elation</text><text x="211" y="143">Nervousness</text><text x="284" y="192">Fear</text><text x="344" y="142">Optimism</text></g>
  </svg>
  <svg class="foot" viewBox="0 0 413 14"><g stroke="var(--navy)" stroke-width="1.5"><line x1="2" y1="2" x2="14" y2="14"/><line x1="8" y1="2" x2="20" y2="14"/><line x1="396" y1="2" x2="408" y2="14"/></g><rect x="22" y="10" width="391" height="3" fill="var(--blue)"/></svg>
</section>

<!-- ROW 6 : headlines -->
<section class="slide col-l" style="top:1451px">
  <div class="topline"></div>
  <div class="title">Behavioral Finance…Beware of Your Emotions</div>
  <div class="mark">Harborline<br>Wealth</div>
  <div class="abs sub" style="left:22px;top:45px">Look Beyond the Headlines</div>
  <div class="abs" style="left:22px;top:59px;width:175px;font-size:6.6px;line-height:1.4;text-align:justify;color:#333">Daily market news and commentary can challenge your investment discipline. Some messages stir anxiety about the future while others tempt you to chase the latest investment fad. When headlines unsettle you, consider the source and maintain a long-term perspective.</div>
  <div class="abs sub" style="left:22px;top:138px">Focus on What you Can Control</div>
  <div class="abs" style="left:22px;top:152px;width:175px;font-size:6.6px;line-height:1.4;text-align:justify;color:#333">A financial advisor can offer expertise and guidance to help you focus on actions that add value. This can lead to a better investment experience.</div>
  <div class="news" style="left:236px;top:41px;width:50px;color:var(--green)">RETIRE RICH</div>
  <div class="news" style="left:262px;top:54px;width:80px;color:var(--blue-dark)">SELL STOCKS NOW</div>
  <div class="news" style="left:236px;top:69px;width:98px;color:#555">THE LOOMING RECESSION</div>
  <div class="news" style="left:228px;top:82px;width:110px;color:var(--green)">THE TOP 10 FUNDS TO OWN</div>
  <div class="news" style="left:254px;top:96px;width:110px;color:var(--blue-dark)">MARKET HITS RECORD HIGH</div>
  <div class="news" style="left:248px;top:110px;width:90px;color:#555">HOUSING MARKET BOOM</div>
  <ul class="blist" style="left:222px;top:133px;width:170px">
    <li>Create an investment plan to fit your needs and risk tolerance.</li>
    <li>Structure a portfolio along the dimensions of expected returns.</li>
    <li>Diversify globally.</li>
    <li>Manage expenses, turnover, and taxes.</li>
    <li>Stay disciplined through market dips and swings.</li>
  </ul>
  <svg class="foot" viewBox="0 0 413 14"><g stroke="var(--navy)" stroke-width="1.5"><line x1="2" y1="2" x2="14" y2="14"/><line x1="8" y1="2" x2="20" y2="14"/><line x1="396" y1="2" x2="408" y2="14"/></g><rect x="22" y="10" width="391" height="3" fill="var(--blue)"/></svg>
</section>

<!-- ROW 6 : relationship features -->
<section class="slide col-r" style="top:1451px">
  <div class="topline"></div>
  <div class="title">Harborline Wealth Relationship</div>
  <div class="mark">Harborline<br>Wealth</div>
  <div class="abs" style="left:27px;top:37px;font-size:10.5px;color:var(--blue)">Organize . Monitor . Collaborate</div>
  <div class="feat-col" style="left:26px;top:71px"><h4>ORGANIZER</h4><p>The production department would then start to manufacture the product, while the marketing department. Some fifty years ago there was a curious case of whale trover litigated.</p></div>
  <div class="feat-col" style="left:123px;top:71px"><h4>INVESTMENTS</h4><p>The production department would then start to manufacture the product, while the marketing department. Some fifty years ago there was a curious case of whale trover litigated.</p></div>
  <div class="feat-col" style="left:221px;top:71px"><h4>SCREEN SHARING</h4><p>The production department would then start to manufacture the product, while the marketing department. Some fifty years ago there was a curious case of whale trover litigated.</p></div>
  <div class="feat-col" style="left:316px;top:71px"><h4>VAULT</h4><p>The production department would then start to manufacture the product, while the marketing department. Some fifty years ago there was a curious case of whale trover litigated.</p></div>
  <div class="feat-col" style="left:26px;top:150px"><h4>TRACK SPENDING</h4><p>The production department would then start to manufacture the product, while the marketing department. Some fifty years ago there was a curious case of whale trover litigated.</p></div>
  <div class="feat-col" style="left:123px;top:150px"><h4>BUDGETING TOOLS</h4><p>The production department would then start to manufacture the product, while the marketing department. Some fifty years ago there was a curious case of whale trover litigated.</p></div>
  <div class="feat-col" style="left:221px;top:150px"><h4>MOBILE</h4><p>The production department would then start to manufacture the product, while the marketing department. Some fifty years ago there was a curious case of whale trover litigated.</p></div>
  <div class="feat-col" style="left:316px;top:150px"><h4>GOALS</h4><p>The production department would then start to manufacture the product, while the marketing department. Some fifty years ago there was a curious case of whale trover litigated.</p></div>
  <svg class="foot" viewBox="0 0 413 14"><g stroke="var(--navy)" stroke-width="1.5"><line x1="2" y1="2" x2="14" y2="14"/><line x1="8" y1="2" x2="20" y2="14"/><line x1="396" y1="2" x2="408" y2="14"/></g><rect x="22" y="10" width="391" height="3" fill="var(--blue)"/></svg>
</section>

<!-- ROW 7 : anywhere -->
<section class="slide col-l" style="top:1702px">
  <div class="topline"></div>
  <div class="title">Anywhere, Anytime</div>
  <div class="mark">Harborline<br>Wealth</div>
  <div class="abs" style="left:30px;top:45px;width:52px;height:130px;border-radius:8px;background:linear-gradient(180deg,#d9dcdf,#9fa6ad)" role="img" aria-label="Smartphone showing the client portal dashboard"></div>
  <div class="abs" style="left:92px;top:45px;width:52px;height:130px;border-radius:8px;background:linear-gradient(180deg,#e3e6e9,#a8afb5)" role="img" aria-label="Smartphone showing the client account list"></div>
  <div class="abs" style="left:185px;top:25px;font-size:4px;font-weight:700;color:var(--blue)">YOUR PERSONAL FINANCIAL WEBSITE</div>
  <div class="abs" style="left:185px;top:32px;font-size:8.5px;color:#333">Take Control of Your Financial World</div>
  <div class="abs" style="left:185px;top:43px;width:150px;font-size:4px;color:#888;line-height:1.3">Your personal financial website makes it easy to manage both your wealth and your well-being.</div>
  <div class="abs" style="left:190px;top:62px;width:190px;height:110px;background:linear-gradient(180deg,#eef1f4,#c3cad1)" role="img" aria-label="Laptop, tablet and desktop screens showing the financial website"></div>
  <div class="abs" style="left:20px;top:189px;width:373px;font-size:6.6px;line-height:1.4;text-align:center;color:#222">More then half of the world's Web traffic is now coming from mobile phones.<br>You will have a consistent and unified experience across all devices – from a mobile phone, tablet, or personal computer – making it easier then ever to use the Client Portal from wherever you are.</div>
  <svg class="foot" viewBox="0 0 413 14"><g stroke="var(--navy)" stroke-width="1.5"><line x1="2" y1="2" x2="14" y2="14"/><line x1="8" y1="2" x2="20" y2="14"/><line x1="396" y1="2" x2="408" y2="14"/></g><rect x="22" y="10" width="391" height="3" fill="var(--blue)"/></svg>
</section>

<!-- ROW 7 : technology partners -->
<section class="slide col-r" style="top:1702px">
  <div class="abs" style="left:19px;top:0;width:128px;height:231px;background:var(--blue)"></div>
  <div class="abs" style="left:33px;top:40px;width:108px;color:#fff;font-size:19px;line-height:1.3">Top Tier Technolog y to Bring Best in Class Service</div>
  <div class="mark">Harborline<br>Wealth</div>
  <div class="partner" style="top:24px"><div class="name">Chartwise</div><p>Chartwise is the firm's principal research platform that can deliver institutional level equity and fixed income coverage of 42,000 equities, mutual funds and ETFs in addition to 400,000 economic tools and indicators.</p></div>
  <div class="partner" style="top:94px"><div class="name" style="font-size:18px">Ledgerly</div><p>Ledgerly is an advanced financial management platform that allows clients to track and monitor all of their investments and liquid wealth in one place, including live reporting on balances, performance, asset allocation, asset location and detailed holding information.</p></div>
  <div class="partner" style="top:160px"><div class="name" style="display:flex;align-items:center;gap:5px;font-size:11px"><span style="width:16px;height:16px;background:var(--blue);display:inline-block"></span>Meridian Tax</div><p>Tax software used by the majority of the nation's top tax firms and businesses for an integrated tax and accounting solution to deliver exceptional tax preparation service designed to minimize a client's income, gift and estate taxes.</p></div>
</section>

<!-- ROW 8 : process steps -->
<section class="slide col-l" style="top:1953px">
  <div class="abs photo-fade" style="inset:0;opacity:.5" role="img" aria-label="Faint photograph of a city skyline"></div>
  <div class="abs" style="inset:0;background:rgba(255,255,255,.7)"></div>
  <div class="abs logo-big" style="left:225px;top:18px;width:110px;font-size:15px">Harborline<br>Wealth</div>
  <div class="abs" style="right:248px;top:55px;text-align:right;font-size:9.5px;line-height:1;color:#222">
    <div>IMAGINE</div>
    <div style="margin-top:18px">TAKING A TRIP</div>
    <div style="margin-top:18px">WITHOUT DIRECTIONS</div>
    <div style="margin-top:18px;font-weight:700">YOU MIGHT MAKE IT<br>TO YOUR DESTINATION</div>
    <div style="margin-top:18px;font-weight:700;font-style:italic">BUT DID YOU TAKE<br>THE BEST ROUTE?</div>
  </div>
  <svg class="abs" style="inset:0" width="413" height="231" viewBox="0 0 413 231">
    <polygon points="230,62 256,40 282,62 270,62 270,120 242,120 242,62" fill="#8c8f93"/>
    <rect x="226" y="112" width="36" height="119" fill="#a7aaae"/>
    <rect x="211" y="142" width="40" height="89" fill="#c2c5c8"/>
    <rect x="198" y="174" width="40" height="57" fill="var(--blue)"/>
    <rect x="183" y="205" width="36" height="26" fill="var(--blue-dark)"/>
  </svg>
  <div class="step-label" style="left:283px;top:77px;line-height:1.3">Ongoing Monitoring &amp;<br>Proactive Financial Guidance</div>
  <div class="step-label" style="left:271px;top:116px">Implement</div>
  <div class="step-label" style="left:257px;top:147px">Develop Plan / Recs</div>
  <div class="step-label" style="left:246px;top:179px">Gather Info &amp; Analyze</div>
  <div class="step-label" style="left:225px;top:212px">Establish / Start Relationship</div>
</section>

<!-- ROW 8 : contact -->
<section class="slide col-r" style="top:1953px">
  <div class="abs" style="left:0;top:0;width:300px;height:231px;background:linear-gradient(135deg,#e6d7c4 0%,#c9a98a 45%,#e9e1d6 100%)" role="img" aria-label="Photograph of a family walking hand in hand on a beach"></div>
  <svg class="abs" style="inset:0" width="413" height="231" viewBox="0 0 413 231">
    <path d="M175,0 H413 V231 H355 Q215,150 175,0 Z" fill="#fff"/>
    <path d="M140,0 L175,0 Q215,150 355,231 L110,231 Q150,130 140,0 Z" fill="var(--blue)"/>
  </svg>
  <div class="abs logo-big" style="left:250px;top:25px;width:150px;font-size:24px">Harborline<br>Wealth</div>
  <div class="contact-heading">Contact<br>Us</div>
  <div class="contact" style="top:118px"><svg width="13" height="13" viewBox="0 0 24 24"><circle cx="12" cy="12" r="11" fill="none" stroke="var(--blue)" stroke-width="2"/><path d="M8,6 l3,0 1,4 -2,1 q1,3 3,4 l1,-2 4,1 0,3 q-9,1 -10,-11Z" fill="var(--blue)"/></svg><span>555 014 2090</span></div>
  <div class="contact" style="top:143px"><svg width="13" height="13" viewBox="0 0 24 24"><rect x="6" y="2" width="12" height="6" fill="var(--blue)"/><rect x="2" y="9" width="20" height="9" rx="2" fill="var(--blue)"/><rect x="6" y="15" width="12" height="7" fill="#fff" stroke="var(--blue)" stroke-width="2"/></svg><span>555 014 6205</span></div>
  <div class="contact" style="top:168px"><svg width="13" height="13" viewBox="0 0 24 24"><path d="M12,2 a7,7 0 0 1 7,7 c0,5 -7,13 -7,13 s-7,-8 -7,-13 a7,7 0 0 1 7,-7Z" fill="var(--blue)"/><circle cx="12" cy="9" r="3" fill="#fff"/></svg><span>48 Harbor Lane,<br>Suite 210<br>Eastport, WA<br>98000</span></div>
</section>

</div>
</body>
</html>
```